Copper Ridge Business Cards For New Startup

I am looking for you to design some business cards for a new startup https://copperridgehub.example. I have supplied logo, brand guidelines and our signatures as a guide.

We need this to reflect the brand guidelines and the website for brand consistency,

What is Copper Ridge?

Mallorca's Business Growth Community
Join your new business community full of passionate entrepreneurs who
love to solve problems and help each other grow together!

Any questions you can ask.

Target Market(s)

Business to Business

Contact Information for Business Card

These are attached (signatures) to the job

Font styles to use
Other font styles liked:
• Open Sans

Requirements
Must have
• Match design guidelines
Nice to have
• Photos of our faces so people remember us

```html
<!DOCTYPE html>
<html lang="en">
<head>
<meta charset="utf-8">
<title>Copper Ridge Business Cards</title>
<link rel="stylesheet" href="https://fonts.googleapis.com/css2?family=Open+Sans:wght@400;600;700&display=swap">
<style>
  :root {
    --page: #e6e4df;
    --earth: #664f22;
    --earth-deep: #5a451c;
    --olive: #66692b;
    --photo-top: #eef0f2;
    --photo-bottom: #8a94a6;
    --ink-light: #ffffff;
  }
  html, body {
    margin: 0;
    width: 960px;
    height: 1200px;
    overflow: hidden;
    background: var(--page);
    font-family: "Open Sans", Arial, sans-serif;
  }
  .sheet { position: relative; width: 960px; height: 1200px; }
  .card {
    position: absolute;
    left: 140px;
    width: 774px;
    height: 432px;
    box-shadow: 0 6px 18px rgba(0,0,0,.25);
  }
  .card--front { top: 110px; }
  .card--back { top: 652px; }
  .card svg { display: block; width: 100%; height: 100%; }
  .earth { fill: var(--earth); }
  .olive { fill: var(--olive); }
  .txt { fill: var(--ink-light); font-family: "Open Sans", Arial, sans-serif; }
  .person-name { font-size: 40px; font-weight: 700; }
  .person-role { font-size: 19px; font-weight: 400; }
  .brand-name { font-size: 36px; font-weight: 600; }
  .brand-name--large { font-size: 48px; }
  .contact { font-size: 30px; font-weight: 700; letter-spacing: 3px; }
  .site { font-size: 34px; font-weight: 700; letter-spacing: 5px; }
  .brand-dot { fill: none; stroke: var(--ink-light); stroke-width: 3; }
</style>
</head>
<body>
<main class="sheet">

  <section class="card card--front" aria-label="Business card front">
    <svg viewBox="0 0 968 540" xmlns="http://www.w3.org/2000/svg">
      <defs>
        <filter id="fold-shadow" x="-10%" y="-10%" width="120%" height="120%">
          <feDropShadow dx="-4" dy="2" stdDeviation="6" flood-color="#000" flood-opacity=".45"/>
        </filter>
        <linearGradient id="photo-fill" x1="0" y1="0" x2="0" y2="1">
          <stop offset="0" stop-color="var(--photo-top)"/>
          <stop offset="1" stop-color="var(--photo-bottom)"/>
        </linearGradient>
      </defs>
      <rect class="earth" width="968" height="540"/>
      <rect class="olive" x="840" y="190" width="128" height="60"/>
      <rect class="olive" x="760" y="355" width="208" height="60"/>
      <polygon class="olive" points="0,0 392,0 392,390 270,480 0,480"/>
      <polygon class="earth" points="270,480 968,0 968,40 470,480" filter="url(#fold-shadow)"/>
      <polygon class="olive" points="460,480 968,5 968,60 690,480" filter="url(#fold-shadow)"/>
      <polygon class="earth" points="680,480 968,60 968,480" filter="url(#fold-shadow)"/>
      <rect class="olive" x="840" y="190" width="128" height="60"/>
      <rect class="olive" x="760" y="355" width="208" height="60"/>
      <polygon class="olive" points="0,540 55,480 968,480 968,540" filter="url(#fold-shadow)"/>
      <rect x="0" y="0" width="345" height="312" fill="url(#photo-fill)" role="img" aria-label="Portrait photo of Daniel Marsh"/>
      <text class="txt person-name" x="176" y="363" text-anchor="middle">Daniel Marsh</text>
      <text class="txt person-role" x="176" y="397" text-anchor="middle">Founder &amp; Growth Hacker</text>
      <circle class="brand-dot" cx="548" cy="75" r="42"/>
      <text class="txt brand-name" x="548" y="162" text-anchor="middle">COPPER RIDGE</text>
      <text class="txt contact" x="112" y="524">+34 611 482 907</text>
      <text class="txt contact" x="958" y="524" text-anchor="end" style="font-size:26px;letter-spacing:2px">dm@copperridgehub.example</text>
    </svg>
  </section>

  <section class="card card--back" aria-label="Business card back">
    <svg viewBox="0 0 968 540" xmlns="http://www.w3.org/2000/svg">
      <defs>
        <filter id="fold-shadow-back" x="-10%" y="-10%" width="120%" height="120%">
          <feDropShadow dx="-4" dy="2" stdDeviation="6" flood-color="#000" flood-opacity=".45"/>
        </filter>
      </defs>
      <rect class="earth" width="968" height="540"/>
      <polygon class="earth" points="260,480 968,0 968,40 470,480" filter="url(#fold-shadow-back)"/>
      <polygon class="olive" points="460,480 968,5 968,60 690,480" filter="url(#fold-shadow-back)"/>
      <polygon class="earth" points="680,480 968,60 968,480" filter="url(#fold-shadow-back)"/>
      <rect class="olive" x="124" y="40" width="166" height="166" rx="12"/>
      <text class="txt brand-name brand-name--large" x="40" y="268">COPPER RIDGE</text>
      <polygon class="olive" points="0,540 95,480 968,480 968,540" filter="url(#fold-shadow-back)"/>
      <text class="txt site" x="935" y="524" text-anchor="end">copperridgehub.example</text>
    </svg>
  </section>

</main>
</body>
</html>
```